Complete Restaurant Branding Project

Bistro Velluto is looking for new ideas and designs for our various branded items.

You will be required to design the following items:

1) Staff Uniforms
2) Dine In Menu
3) Take Out Menu
4) Food Take Out Packaging
5) Take Out Bags
6) Beverage Take Out Cups
7) Dine in plates, coffee cups, mugs, etc...
8) Feel free to design any other brandable items related to our business

Please check our website to get a feel of our restaurant. Make sure to check the menu and the different dishes we offer to help you in the food packaging design and menu design. http://www.bistrovelluto-example.com/

We are open to new ideas, so we intentionally won't specify details such as materials, sizes, or shapes for any item.

We refined our logo in a contest a few days ago, the new logo is attached. Please don't use the logo from the website or any graphic elements from the website theme in your designs.

```html
<!DOCTYPE html>
<html lang="en">
<head>
<meta charset="utf-8">
<title>Bistro Velluto – Pizza Box</title>
<link rel="stylesheet" href="https://fonts.googleapis.com/css2?family=Alegreya+SC:wght@700&family=Lato:wght@400&display=swap">
<style>
  :root {
    --backdrop-light: #efefef;
    --backdrop-dark: #8e8e8e;
    --lid-white: #f6f6f3;
    --mustard: #e2b531;
    --mustard-mid: #d6a827;
    --mustard-deep: #c8961c;
    --mustard-glow: #ecc64a;
    --brown-deep: #3f1f0f;
    --brown-soft: #5a2e17;
    --rim: #a8822e;
    --logo-brown: #7b3314;
    --gold-text: #e6bb3c;
    --hole: #0d0d0d;
  }
  * { margin: 0; padding: 0; box-sizing: border-box; }
  html, body { width: 1200px; height: 960px; overflow: hidden; }
  body {
    background: radial-gradient(ellipse at 50% 72%, var(--backdrop-light) 0%, #d2d2d2 55%, var(--backdrop-dark) 100%);
    font-family: "Lato", sans-serif;
    position: relative;
  }
  .pizza-box {
    position: absolute;
    left: 260px;
    top: 110px;
    width: 680px;
    box-shadow: 0 18px 40px rgba(0,0,0,0.18);
  }
  .lid {
    position: relative;
    width: 680px;
    height: 620px;
    background: var(--lid-white);
    overflow: hidden;
  }
  .lid-pattern {
    position: absolute;
    left: 0;
    right: 0;
    top: 260px;
    bottom: 0;
    background:
      radial-gradient(ellipse 60% 45% at 30% 35%, rgba(236,198,74,0.55) 0%, rgba(236,198,74,0) 70%),
      radial-gradient(ellipse 55% 50% at 78% 70%, rgba(200,150,28,0.5) 0%, rgba(200,150,28,0) 70%),
      linear-gradient(160deg, var(--mustard) 0%, var(--mustard-mid) 55%, var(--mustard-deep) 100%);
  }
  .brand-mark {
    position: absolute;
    left: 0;
    right: 0;
    top: 200px;
    display: flex;
    flex-direction: column;
    align-items: center;
  }
  .brand-mark .seal { display: block; }
  .brand-name {
    margin-top: 18px;
    font-family: "Alegreya SC", serif;
    font-weight: 700;
    font-size: 42px;
    line-height: 1;
    letter-spacing: 2px;
    color: var(--logo-brown);
  }
  .brand-tagline {
    margin-top: 12px;
    font-family: "Alegreya SC", serif;
    font-weight: 700;
    font-size: 20px;
    line-height: 1;
    letter-spacing: 1px;
    color: var(--logo-brown);
  }
  .front-panel {
    position: relative;
    width: 680px;
    height: 100px;
    border-top: 6px solid var(--rim);
  }
  .front-panel .panel-fill {
    position: absolute;
    inset: 0;
    background:
      radial-gradient(ellipse 40% 80% at 35% 50%, rgba(110,58,30,0.5) 0%, rgba(110,58,30,0) 70%),
      linear-gradient(90deg, var(--brown-deep), var(--brown-soft) 50%, var(--brown-deep));
  }
  .front-panel svg { position: absolute; inset: 0; }
  .web-address {
    position: absolute;
    right: 84px;
    top: 36px;
    font-size: 19px;
    line-height: 22px;
    letter-spacing: 0.5px;
    color: var(--gold-text);
    white-space: nowrap;
  }
</style>
</head>
<body>
  <div class="pizza-box">
    <section class="lid">
      <div class="lid-pattern" role="img" aria-label="Mustard floral pattern covering the lower lid"></div>
      <div class="brand-mark">
        <svg class="seal" width="110" height="110" viewBox="0 0 110 110" aria-hidden="true">
          <circle cx="55" cy="55" r="54" fill="var(--logo-brown)"/>
        </svg>
        <div class="brand-name">Bistro Velluto</div>
        <div class="brand-tagline">Cafe &amp; Restaurant</div>
      </div>
    </section>
    <section class="front-panel">
      <div class="panel-fill" role="img" aria-label="Dark brown floral pattern along the box side"></div>
      <svg width="680" height="94" viewBox="0 0 680 94" aria-hidden="true">
        <circle cx="40" cy="47" r="22" fill="var(--hole)"/>
        <circle cx="640" cy="47" r="22" fill="var(--hole)"/>
        <circle cx="110" cy="47" r="13" fill="var(--gold-text)"/>
        <circle cx="150" cy="47" r="13" fill="var(--gold-text)"/>
        <circle cx="190" cy="47" r="13" fill="var(--gold-text)"/>
      </svg>
      <div class="web-address">www.bistrovelluto-example.com</div>
    </section>
  </div>
</body>
</html>
```